Number of Pages Required

1 page

Requirements
Must have
• An Overview / Background of the Business & Services(not for profit rescue animal farm)
• The Target Market / Audience you are trying to reach (animal lovers)
• Design Specifics; any preferences or ideas for Style, Colour, Imagery, etc (no preferences)

```html
<!DOCTYPE html>
<html lang="en">
<head>
<meta charset="utf-8">
<title>Green Pasture – Rescue Animal Farm</title>
<link rel="stylesheet" href="https://fonts.googleapis.com/css2?family=Merriweather:ital,wght@0,300;0,400;0,700;1,400&family=Merriweather+Sans:wght@300;400;700&family=Ubuntu:wght@500;700&display=swap">
<style>
:root{
  --grass-dark:#4d7a1e;
  --grass-light:#9cc456;
  --yellow:#f4c81a;
  --yellow-deep:#eab90c;
  --ink:#2b2b2b;
  --muted:#6d6d6d;
  --teal:#1f8a8a;
  --grey-bg:#ecedeb;
  --cell-bg:#f5f5f3;
  --tag:#d8c59a;
  --white:#ffffff;
  --sky-warm:#f6d46b;
}
*{box-sizing:border-box;margin:0;padding:0}
html,body{width:1200px;height:3209px;overflow:hidden}
body{position:relative;background:var(--white);font-family:"Merriweather",Georgia,serif;color:var(--ink)}
.abs{position:absolute}
.divider{position:absolute;width:160px;height:14px}
.front{z-index:2}

/* hero */
.hero{left:0;top:0;width:1200px;height:610px;background:linear-gradient(180deg,#8fb44f 0%,#6f9c2f 30%,#5e8c25 65%,#4b7719 100%)}
.nav{right:128px;top:32px;display:flex;gap:6px;font-family:"Merriweather Sans",Arial,sans-serif;font-size:13px;color:var(--white)}
.nav a{color:var(--white);text-decoration:none;padding:8px 14px}
.nav a.active{border:1px solid rgba(255,255,255,.8)}
.hero-title{right:82px;top:254px;text-align:right;font-family:"Ubuntu",Arial,sans-serif;font-weight:700;font-size:29px;line-height:36px;color:var(--white);letter-spacing:.5px}

/* features */
.features{left:0;top:610px;width:1200px;height:241px;background:linear-gradient(180deg,var(--yellow) 0%,var(--yellow-deep) 100%)}
.feature{position:absolute;top:40px;width:300px;text-align:center}
.feature svg{display:block;margin:0 auto 10px}
.feature h3{font-size:11px;font-weight:700;color:#3a2e08;margin-bottom:10px;text-transform:uppercase}
.feature p{font-size:10.5px;line-height:17px;color:#7a5d05}

/* residents */
.section-title{position:absolute;width:100%;text-align:center;font-family:"Merriweather Sans",Arial,sans-serif;font-weight:300;font-size:29px;color:var(--ink)}
.grid{left:128px;top:999px;width:942px;height:314px;display:grid;grid-template-columns:repeat(6,157px);grid-template-rows:repeat(2,157px)}
.photo{display:block}
.resident{background:var(--cell-bg);text-align:center;padding-top:38px}
.resident h4{font-size:11px;font-weight:700;margin-bottom:10px}
.resident p{font-size:10px;line-height:16px;color:var(--muted);padding:0 14px}
.resident .age{font-size:11px;color:var(--ink);margin-top:8px}

/* about */
.about{left:0;top:1380px;width:1200px;height:605px;background:var(--grey-bg)}
.about h2{position:absolute;left:116px;width:400px;top:146px;text-align:center;font-family:"Merriweather Sans",Arial,sans-serif;font-weight:300;font-size:29px}
.about p{position:absolute;left:116px;width:400px;top:246px;text-align:center;font-size:17px;line-height:34px;font-weight:300}
.about-photo{left:548px;top:85px;width:631px;height:422px;background:linear-gradient(180deg,#d9b3a8 0%,#b8a48a 40%,#5f7a3a 75%,#3d5a22 100%)}

/* blog */
.more{font-size:10px;font-style:italic;color:var(--teal)}
.blog-title{position:absolute;width:100%;text-align:center;top:2028px;font-family:"Merriweather Sans",Arial,sans-serif;font-weight:400;font-size:26px;color:var(--ink)}
.news-label{left:180px;top:2096px;font-family:"Ubuntu",Arial,sans-serif;font-size:11px;font-weight:700;letter-spacing:1.5px}
.news-label span{font-family:"Merriweather",Georgia,serif;font-weight:400;letter-spacing:0;font-size:9px;color:var(--teal);font-style:italic;margin-left:10px}
.post-img{width:203px;height:137px}
.post{width:356px}
.post h3{font-size:17px;line-height:21px;font-weight:400;color:var(--teal)}
.post .meta{font-size:9px;font-style:italic;color:var(--muted);margin:4px 0 10px}
.post .meta b{font-weight:400;color:var(--teal)}
.post .excerpt{font-size:9.5px;line-height:15px;color:var(--muted)}
.post .foot{display:flex;align-items:center;gap:8px;margin-top:12px;font-size:10px;font-style:italic;color:var(--muted)}
.comments{background:var(--tag);color:#fff;font-size:8px;padding:3px 8px;font-style:normal;margin-right:14px}
.sq{width:13px;height:13px;background:#3f6fb5;display:inline-block}
.sq.b{background:#3aa6d8}
.foot .tags b{font-weight:400;color:var(--teal)}

.video{left:811px;top:2105px;width:370px;height:231px;background:linear-gradient(180deg,#6a7a3a 0%,#8a9a4a 40%,#3c4a26 100%)}
.side-small{font-size:8px;line-height:12px;color:var(--muted)}
.side-small i{color:var(--teal)}
.vote h5{font-family:"Ubuntu",Arial,sans-serif;font-size:10px;letter-spacing:1px;margin-bottom:10px}
.vote li{list-style:none;font-size:8px;line-height:12px;color:var(--muted);margin-bottom:7px;display:flex;gap:10px}
.vote li::before{content:"";width:6px;height:6px;border:1px solid #999;border-radius:50%;flex:none;margin-top:3px}
.btn{background:var(--tag);color:#fff;font-size:8px;padding:4px 14px;display:inline-block}

/* contact */
.contact{left:0;top:2600px;width:1200px;height:609px;background:linear-gradient(180deg,rgba(251,231,163,0) 0%,#fbe7a3 6%,var(--sky-warm) 35%,#e9b64a 62%,#a9b04a 80%,#7a9a2e 100%)}
.contact h2{position:absolute;left:738px;top:52px;font-family:"Merriweather Sans",Arial,sans-serif;font-weight:300;font-size:26px}
.col{position:absolute;top:140px;font-size:11px;line-height:17px;color:var(--ink)}
.col h4{font-family:"Merriweather Sans",Arial,sans-serif;font-weight:400;font-size:12px;margin-bottom:6px}
.form-label{left:710px;top:252px;font-family:"Merriweather Sans",Arial,sans-serif;font-size:11px}
.field{position:absolute;border-bottom:1px solid var(--ink);font-size:11px;font-style:italic;padding-bottom:3px}
.search{left:1001px;top:52px;width:128px;height:16px;border-radius:8px;background:rgba(255,255,255,.75)}
</style>
</head>
<body>

<header class="abs hero" role="img" aria-label="Photo of sheep grazing on a green meadow"></header>
<nav class="abs nav">
  <a class="active" href="#">Home</a><a href="#">Residents</a><a href="#">About</a><a href="#">Visit</a><a href="#">Contact</a>
</nav>
<h1 class="abs hero-title">EVERY ANIMAL DESERVES A HOME,<br>A GREEN FIELD AND A FRIEND.</h1>
<svg class="divider" style="left:880px;top:354px" viewBox="0 0 160 14"><line x1="0" y1="7" x2="160" y2="7" stroke="#fff"/><rect x="74" y="1" width="12" height="12" transform="rotate(45 80 7)" fill="#fff"/></svg>

<section class="abs features">
  <div class="feature" style="left:96px">
    <svg width="56" height="46" viewBox="0 0 56 46" fill="none" stroke="#2b2b2b" stroke-width="2"><path d="M6 20h44c0 14-10 22-22 22S6 34 6 20z"/><line x1="30" y1="18" x2="50" y2="2"/><line x1="36" y1="18" x2="54" y2="6"/></svg>
    <h3>Rescue &amp; care</h3>
    <p>We take in farm animals saved from neglect<br>and give each one food, shelter and a vet<br>for the rest of its life</p>
  </div>
  <div class="feature" style="left:434px">
    <svg width="70" height="46" viewBox="0 0 70 46" fill="none" stroke="#2b2b2b" stroke-width="2"><path d="M16 16h36v14c0 8-8 12-18 12s-18-4-18-12z"/><path d="M52 20c8 0 10 10 0 12"/><path d="M16 22L4 14"/><circle cx="34" cy="10" r="4"/></svg>
    <h3>Visit the farm</h3>
    <p>Come for tea in the meadow on weekends,<br>meet the flock and help at feeding time<br>with our volunteers</p>
  </div>
  <div class="feature" style="left:802px">
    <svg width="46" height="46" viewBox="0 0 46 46" fill="none" stroke="#2b2b2b" stroke-width="2"><path d="M8 20c0-10 30-10 30 0z"/><path d="M10 20l4 22h18l4-22"/><line x1="20" y1="22" x2="21" y2="42"/><line x1="26" y1="22" x2="25" y2="42"/></svg>
    <h3>Get social</h3>
    <p>Follow daily news from the barn, share<br>rescue stories with friends and join<br>our caring community</p>
  </div>
</section>

<h2 class="section-title" style="top:892px">This month residents</h2>
<svg class="divider" style="left:520px;top:945px" viewBox="0 0 160 14"><line x1="0" y1="7" x2="160" y2="7" stroke="#333"/><rect x="74" y="1" width="12" height="12" transform="rotate(45 80 7)" fill="#333"/></svg>

<div class="abs grid">
  <div class="photo" role="img" aria-label="Photo of calves in a field" style="background:linear-gradient(180deg,#8aa856,#6b5236)"></div>
  <div class="resident"><h4>Clover</h4><p>Rescued calf, loves the morning sun</p><div class="age">Age 2</div></div>
  <div class="photo" role="img" aria-label="Photo of a sheep and a cow on grass" style="background:linear-gradient(180deg,#a9c36a,#c79a5e)"></div>
  <div class="resident"><h4>Bramble &amp; Rosie</h4><p>Best friends who share one stall</p><div class="age">Age 6</div></div>
  <div class="photo" role="img" aria-label="Photo of a white calf lying down" style="background:linear-gradient(180deg,#cfd3c8,#8a9a6a)"></div>
  <div class="resident"><h4>Snowdrop</h4><p>Gentle calf saved last winter</p><div class="age">Age 1</div></div>
  <div class="resident"><h4>The herd</h4><p>Four cows retired from dairy work</p><div class="age">Age 9</div></div>
  <div class="photo" role="img" aria-label="Photo of cows and a sheep in a pasture" style="background:linear-gradient(180deg,#9fb77a,#5b6b3a)"></div>
  <div class="resident"><h4>Hazel</h4><p>Curious goat, first to greet guests</p><div class="age">Age 4</div></div>
  <div class="photo" role="img" aria-label="Photo of a brown goat" style="background:linear-gradient(180deg,#c9a57c,#7a4a2a)"></div>
  <div class="resident"><h4>Marigold</h4><p>Hen rescued from a cage farm</p><div class="age">Age 3</div></div>
  <div class="photo" role="img" aria-label="Photo of a hen" style="background:linear-gradient(180deg,#f2e7d6,#b8582a)"></div>
</div>

<section class="abs about">
  <h2>About us</h2>
  <svg class="divider" style="left:236px;top:198px" viewBox="0 0 160 14"><line x1="0" y1="7" x2="160" y2="7" stroke="#333"/><rect x="74" y="1" width="12" height="12" transform="rotate(45 80 7)" fill="#333"/></svg>
  <p>Green Pasture is a not-for-profit farm where rescued sheep, cows, goats and hens live out their lives in peace, cared for by animal lovers.</p>
  <div class="abs about-photo" role="img" aria-label="Photo of a child sitting among black lambs on grass"></div>
</section>
<div class="abs more" style="left:331px;top:1992px">more pictures</div>

<h2 class="blog-title">BLOG</h2>
<svg class="divider" style="left:520px;top:2074px" viewBox="0 0 160 14"><line x1="0" y1="7" x2="160" y2="7" stroke="#333"/><rect x="74" y="1" width="12" height="12" transform="rotate(45 80 7)" fill="#333"/></svg>
<div class="abs news-label">LATEST NEWS<span>more news</span></div>

<div class="abs post-img" style="left:180px;top:2122px;background:linear-gradient(180deg,#e9e4dc,#6b5a48)" role="img" aria-label="Photo of a calf looking into the camera"></div>
<article class="abs post" style="left:406px;top:2118px">
  <h3>Twelve calves found a new home on the farm this spring</h3>
  <div class="meta">12 Jul, 2021 • from <b>Mara Lindqvist</b></div>
  <p class="excerpt">Our volunteers drove through the night to bring the calves home. After a week of rest and warm milk they now run the meadow every morning.</p>
  <div class="foot"><span class="comments">12 COMMENTS</span><span class="sq"></span><span class="sq b"></span><span class="tags">Tags: <b>Rescue, Calves, Spring</b></span></div>
</article>

<div class="abs post-img" style="left:180px;top:2293px;background:linear-gradient(180deg,#9bb46a,#4e3a2a)" role="img" aria-label="Photo of a child hugging a cow"></div>
<article class="abs post" style="left:406px;top:2289px">
  <h3>Family days: meet and hug the animals in the barn</h3>
  <div class="meta">12 Jul, 2021 • from <b>Mara Lindqvist</b></div>
  <p class="excerpt">Every Saturday families can join feeding time, brush the cows and learn how each resident was rescued. Children love the gentle herd.</p>
  <div class="foot"><span class="comments">12 COMMENTS</span><span class="sq"></span><span class="sq b"></span><span class="tags">Tags: <b>Visits, Family, Cows</b></span></div>
</article>

<div class="abs post-img" style="left:180px;top:2466px;background:linear-gradient(180deg,#eeece6,#a9a294)" role="img" aria-label="Photo of a sheep close up"></div>
<article class="abs post front" style="left:406px;top:2462px">
  <h3>Shearing season keeps our rescued flock cool and happy</h3>
  <div class="meta">12 Jul, 2021 • from <b>Mara Lindqvist</b></div>
  <p class="excerpt">With summer coming, each sheep got a gentle trim. The wool is spun by local friends and sold to pay for hay and vet care.</p>
  <div class="foot"><span class="comments">12 COMMENTS</span><span class="sq"></span><span class="sq b"></span><span class="tags">Tags: <b>Sheep, Summer, Care</b></span></div>
</article>

<div class="abs video" role="img" aria-label="Video still of animals in the farm barn"></div>
<svg class="abs" style="left:978px;top:2202px" width="36" height="36" viewBox="0 0 36 36"><circle cx="18" cy="18" r="17" fill="rgba(255,255,255,.85)"/><path d="M14 11l11 7-11 7z" fill="#333"/></svg>
<div class="abs side-small" style="left:1002px;top:2338px;width:180px"><i>A day in the life of the barn</i><br>Follow the flock from sunrise feeding to the evening walk back in from the meadow.</div>
<div class="abs side-small" style="left:808px;top:2388px">Tags: <i>Barn, Video, Daily life</i></div>
<div class="abs side-small" style="left:808px;top:2518px">Tags: <i>Barn, Video, Daily life</i></div>
<div class="abs side-small front" style="left:907px;top:2560px"><i>all videos</i></div>
<div class="abs vote front" style="left:1003px;top:2426px;width:130px">
  <h5>VOTE</h5>
  <p class="side-small" style="margin-bottom:8px">Which weekend event would you like to join on the farm?</p>
  <ul><li>Feeding time</li><li>Barn tours</li><li>Shearing day</li><li>Volunteer garden work</li></ul>
</div>

<section class="abs contact" role="img" aria-label="Illustration of an autumn farmyard with a thatched hut, rooster and flowers under a golden sky">
  <div class="abs search"></div>
  <span class="abs sq" style="left:1003px;top:76px"></span><span class="abs sq b" style="left:1020px;top:76px"></span><span class="abs sq" style="left:1037px;top:76px;background:#f08a24"></span>
  <h2>Contact</h2>
  <svg class="divider" style="left:710px;top:94px" viewBox="0 0 160 14"><line x1="0" y1="7" x2="160" y2="7" stroke="#333"/><rect x="74" y="1" width="12" height="12" transform="rotate(45 80 7)" fill="#333"/></svg>
  <div class="col" style="left:710px"><h4>GREEN PASTURE</h4>118 Orchard Lane<br>Millbrook, VT 05901</div>
  <div class="col" style="left:935px"><h4>VISITS</h4>hello@greenpasture.org<br>+1 555-0142</div>
  <div class="abs form-label">CONTACT FORM</div>
  <div class="field" style="left:710px;top:284px;width:160px">Name</div>
  <div class="field" style="left:915px;top:284px;width:155px">Email</div>
  <div class="field" style="left:722px;top:348px;width:150px;border:none">Message</div>
</section>

</body>
</html>
```